Coaching company requires a Bi-Fold Services Brochure

**Please also read attached design brief***

As part of our expanding sales role for our Professional Development Company, we need a Bi-Fold services brochure that offers our clients some further information about our specific services.

This services brochure will be the document that our clients will receive after our initial contact with them so the overall design of this document will play an instrumental part in our securing of ongoing work.

We have prepared a design brief for designers that want to undertake this task and this document should help to clarify any missing information from this online brief. Any designer who is interested in submitting a design should also refer to this attached document to get the full scope of the works required.

Regular email correspondence will also be available to clarify any questions that the design may have

*** Please also note that the finished design will need to be submitted in a PSD format to allow for editing in Photoshop CS6

Target Market(s)

Our target market is Business to Business. We are specifically targeting small, medium and large businesses who are looking to invest in Professional Development for their business and their staff.
The areas of major focus are 1 on 1 coaching of leaders, executives & business owners and group facilitation sessions with their staff.

Industry/Entity Type

Business Service

Font styles to use
Sans Serif

Requirements
Must have
• - Design needs to be an A4 Bi-Fold layout so should suit an A3 sheet of paper (297mm x 420mm)
• - Include our corporate color scheme
• - Finished design must be in PSD format or format that can be edited in Photshop CS6
• - Appealing to small, medium and large businesses (universal appeal)
• - The project must be in CMYK Colour and no less than 300 pixel resolution
Nice to have
• - Our logo incorporated into the front page
• - We would like the images used in this brochure to be happy and vibrant (i.e. smiling faces and energetic etc.)

```html
<!DOCTYPE html>
<html lang="en">
<head>
<meta charset="utf-8">
<title>Northvale PD – Services Brochure, Page 02</title>
<link rel="stylesheet" href="https://fonts.googleapis.com/css2?family=Arimo:wght@400&family=Roboto+Condensed:wght@700&display=swap">
<style>
  :root {
    --page: #f2f2f3;
    --brand-blue: #1b9ad9;
    --ink: #1d1d1f;
    --white: #ffffff;
    --accent-red: #e0282e;
  }
  * { box-sizing: border-box; margin: 0; padding: 0; }
  html, body { width: 1008px; height: 1200px; overflow: hidden; background: var(--page); }
  body { position: relative; font-family: "Arimo", Arial, sans-serif; color: var(--ink); }

  .hero-photo {
    position: absolute; left: 69px; top: 58px; width: 530px; height: 298px;
    background: linear-gradient(135deg, #c9d3da 0%, #5d7d99 40%, #2e4a66 65%, #b9a88c 100%);
  }

  .section-title {
    font-family: "Roboto Condensed", "Arial Narrow", sans-serif;
    font-weight: 700; color: var(--brand-blue);
    font-size: 46px; line-height: 1; letter-spacing: -1.5px; text-transform: uppercase;
  }
  .body-copy p { font-size: 17.5px; line-height: 22.8px; margin-bottom: 22.8px; }
  .body-copy p:last-child { margin-bottom: 0; }

  .intro-title { position: absolute; left: 69px; top: 402px; }
  .intro-copy { position: absolute; left: 69px; top: 460px; width: 505px; }
  .results-title { position: absolute; left: 69px; top: 893px; }
  .results-copy { position: absolute; left: 69px; top: 955px; width: 512px; }

  .values-panel {
    position: absolute; left: 599px; top: 58px; width: 339px; height: 1082px;
    background: var(--brand-blue); color: var(--white); text-align: center;
  }
  .value { position: absolute; left: 22px; right: 22px; }
  .value-purpose { top: 27px; }
  .value-vision { top: 213px; }
  .value-mission { top: 447px; }
  .value-icon {
    display: block; margin: 0 auto; width: 44px; height: 44px;
    border: 3px solid var(--accent-red); border-radius: 50%;
  }
  .value-title {
    font-family: "Roboto Condensed", "Arial Narrow", sans-serif;
    font-weight: 700; font-size: 27px; letter-spacing: -0.5px; text-transform: uppercase;
    line-height: 1; margin: 22px 0 9px;
  }
  .value p { font-size: 15.5px; line-height: 18.7px; margin-bottom: 18.7px; }
  .value p:last-child { margin-bottom: 0; }

  .page-footer {
    position: absolute; left: 69px; top: 1152px;
    display: flex; align-items: center; gap: 8px;
    font-family: "Roboto Condensed", "Arial Narrow", sans-serif; font-weight: 700;
    font-size: 16px; letter-spacing: -0.3px; color: var(--ink);
  }
  .footer-dot { width: 12px; height: 12px; border-radius: 50%; background: var(--brand-blue); }
  .page-number { border-left: 1.5px solid var(--ink); padding-left: 8px; margin-left: 10px; }
</style>
</head>
<body>
  <div class="hero-photo" role="img" aria-label="Businessman in a suit touching a digital screen overlaid with a city skyline and growth chart"></div>

  <h2 class="section-title intro-title">About Us</h2>
  <div class="body-copy intro-copy">
    <p>Northvale PD is a professional development company, who specialises in assisting all levels of business with the development of their most valued asset… Their people!</p>
    <p>Working closely with our clients, we assist them to build and adopt highly successful “people centric” cultures and philosophies that resonate throughout their entire business.</p>
    <p>From front line operators all the way to the treatment of your clients, we help your business to ingrain an everlasting “human focused” principals that increase personal performance, drive innovation and change, increase customer satisfaction levels, ensure repeat business and builds a reputation for your business that outshines your competitors!</p>
  </div>

  <h2 class="section-title results-title">How We Deliver Results:</h2>
  <div class="body-copy results-copy">
    <p>From tailored Leadership development coaching to the design and delivery of operational strategies, we are with you every step of the way! After establishing your businesses unique requirements, we utilise a multiple of different professional development services to help you establish a strong “people centric” culture and philosophy across your entire business structure.</p>
  </div>

  <aside class="values-panel">
    <div class="value value-purpose">
      <span class="value-icon"></span>
      <h3 class="value-title">Our Purpose</h3>
      <p>or reason for existing; is to empower the talented to achieve the extraordinary</p>
    </div>
    <div class="value value-vision">
      <span class="value-icon"></span>
      <h3 class="value-title">Our Vision</h3>
      <p>is to raise the quality of life for all Kelbrook locals through the indoctrination of a “people-centric” work culture into Kelbrook businesses.</p>
    </div>
    <div class="value value-mission">
      <span class="value-icon"></span>
      <h3 class="value-title">Our Mission</h3>
      <p>to deliver on our Vision; we will work hand in hand with businesses and new, existing and emerging business leaders to demonstrate the values and benefits of a people centric leadership philosophy. This influence will usher in a new generation of business leaders that will ultimately contribute and drive the future growth and development of the community in which they work.</p>
      <p>Through the expert delivery of our professional development services, we will help to create a region where each and every person will know their true personal &amp; professional value and who will embrace their career with the same gusto and passion as they do their life.</p>
      <p>We will do all of this; within an environment that is fun, friendly, open, honest and conducive to the collective values and beliefs of our clients.</p>
    </div>
  </aside>

  <footer class="page-footer">
    <span class="footer-dot"></span>
    <span>SERVICES BROCHURE</span>
    <span class="page-number">02</span>
  </footer>
</body>
</html>
```